High End Notary Service Business Card Design

Want a professional and elegant/luxurious business card that is clean and simple in the design. A notary is a trusted professional that helps people sign very important documents. The card should be in alignment with this service provided.

Most of the time, service will be for the purchase of a home or refinance of a mortgage

There is NO LOGO. This is aesthetic. A look and feel. Conveying professionalism and concierge level of service.

Target Market(s)

Other business professionals, Lawyers, Escrow Officers, Loan Officers

Industry/Entity Type

Legal

Contact Information for Business Card

This will be a one-sided business card

Colors
35a7d7
3176b5
85cae6
d3a5cc
b868aa
ffffff
0356a4

Requirements
Must have
• Doreen L. Marsh-Whitlock
Notary Public

614-872-3916
MarshPublicNotary@Vornmail.com
Nice to have
• Headshot photo below. Convey the aspect of signing documents. No black cards. Preference is shades of blue: light blue, navy, aqua, gold, white, or lavendar, etc.
Should not have
• No scales or legal scales.

```html
<!DOCTYPE html>
<html lang="en">
<head>
<meta charset="utf-8">
<title>Doreen L. Marsh-Whitlock — Notary Public</title>
<link rel="stylesheet" href="https://fonts.googleapis.com/css2?family=Montserrat:wght@400;500;800&display=swap">
<style>
  :root {
    --backdrop: #e6e6e4;
    --card: #ffffff;
    --ink: #2a2a2a;
    --ink-soft: #3a3a3a;
    --rule-deep: #0356a4;
    --rule-mid: #3176b5;
    --accent-aqua: #35a7d7;
    --accent-navy: #3176b5;
  }
  * { margin: 0; padding: 0; box-sizing: border-box; }
  html, body {
    width: 1200px;
    height: 800px;
    overflow: hidden;
    background: var(--backdrop);
  }
  .canvas {
    width: 1200px;
    height: 800px;
    display: flex;
    align-items: center;
    justify-content: center;
  }
  .business-card {
    width: 1050px;
    height: 600px;
    background: var(--card);
    box-shadow: 0 14px 40px rgba(0, 0, 0, 0.12), 0 2px 6px rgba(0, 0, 0, 0.08);
    display: flex;
    flex-direction: column;
    align-items: center;
    font-family: "Montserrat", sans-serif;
    color: var(--ink);
    text-align: center;
  }
  .identity {
    margin-top: 150px;
  }
  .holder-name {
    font-weight: 800;
    font-size: 54px;
    letter-spacing: 0.5px;
    color: var(--ink);
  }
  .holder-title {
    margin-top: 8px;
    font-weight: 400;
    font-size: 34px;
    letter-spacing: 1.5px;
    color: var(--ink-soft);
  }
  .divider {
    width: 860px;
    height: 2px;
    margin-top: 22px;
    background: linear-gradient(90deg,
      rgba(49, 118, 181, 0) 0%,
      var(--rule-mid) 30%,
      var(--rule-deep) 55%,
      var(--rule-mid) 80%,
      rgba(49, 118, 181, 0) 100%);
  }
  .contact {
    margin-top: 22px;
    font-weight: 400;
    color: var(--ink);
  }
  .contact-phone {
    font-size: 36px;
    letter-spacing: 1.5px;
  }
  .contact-email {
    margin-top: 8px;
    font-size: 36px;
    letter-spacing: 0.5px;
  }
  .accent-mark {
    margin-top: 30px;
  }
</style>
</head>
<body>
  <main class="canvas">
    <section class="business-card">
      <header class="identity">
        <h1 class="holder-name">Doreen L. Marsh-Whitlock</h1>
        <p class="holder-title">Notary Public</p>
      </header>
      <div class="divider"></div>
      <div class="contact">
        <p class="contact-phone">614-872-3916</p>
        <p class="contact-email">MarshPublicNotary@Vornmail.com</p>
      </div>
      <svg class="accent-mark" width="120" height="36" viewBox="0 0 120 36" role="img" aria-label="Small blue decorative accent">
        <rect x="0" y="0" width="120" height="36" fill="var(--accent-aqua)"/>
      </svg>
    </section>
  </main>
</body>
</html>
```